依頼詳細
http://www.kazane-mori.jp/
こちらのデザイン変更をお願いしたいと思っています。
取り扱い商品も「森花詩」ブランドのみにまずは絞ります。現在新商品を開発中なので、5~6アイテム程度になる予定です。
自然系の商品なので、ナチュラルな感じのサイトがいいと思っています。
https://www.tokura-ken.co.jp/
http://www.berufonte.co.jp/
戸倉研究所やベルフォンテがベンチマークです。
トップページと商品ページのデザインをお願いできればと思います。
サイトURL
ページ数
2ページ
希望イメージ
シンプル 複雑
単色 カラフル
暗い 明るい
日常 高級
遊び心 厳粛
未来的 伝統的
女性的 男性的
希望する色
納品ファイル
補足説明
何名様からかご質問あったコーディングについてはmustではありません。
まずはデザインのご提案をお待ちしております。
※デザインを選ばせていただいた方がコーディングできる場合は、別途コーディングもお願いさせていただきます。
(プラスお支払します。)
hm-takegawa.co.jpから情報を引用することは問題ありません。
よろしくお願いいたします。
■ 選んだ理由

取り急ぎ選ばせていただきました。
後日修正点を御連絡いたします。その上で納品ください。
また、下記別途で構いませんので対応可能でしょうか?
・コーディング
・バナー作成
可能な場合、金額もお知らせください。
よろしくお願いします。

■ 提案者全員のお礼・コメント

この度はご提案ありがとうございます。
またよろしくお願い致します。

```html
<!DOCTYPE html>
<html lang="ja">
<head>
<meta charset="utf-8">
<title>KAZANEMORI オンラインショップ</title>
<link href="https://fonts.googleapis.com/css2?family=Noto+Sans+JP:wght@400;700&family=Noto+Serif+JP:wght@500;700&family=Cormorant+Garamond:wght@600&display=swap" rel="stylesheet">
<style>
:root{
  --bg:#f4efe6;
  --paper:#ffffff;
  --brown:#6e5138;
  --brown-dark:#4c3625;
  --beige:#e6dccb;
  --line:#d9cdb9;
  --green:#86b23a;
  --green-dark:#5f8a22;
  --orange:#e07a2a;
  --red:#b5321e;
  --text:#4a3b2e;
  --muted:#8c7b69;
}
*{box-sizing:border-box;margin:0;padding:0}
html,body{width:1200px;height:2436px;overflow:hidden}
body{background:var(--bg);font-family:"Noto Sans JP",sans-serif;color:var(--text);font-size:12px;line-height:1.5}
a{color:inherit;text-decoration:none}

.site-header{height:86px;background:linear-gradient(#fffdf8,#f6f0e4);position:relative}
.tagline{position:absolute;left:124px;top:10px;font-size:10px;color:var(--muted);line-height:1.4}
.logo{position:absolute;left:0;right:0;top:14px;text-align:center;font-family:"Cormorant Garamond",serif;font-weight:600;font-size:38px;letter-spacing:4px;color:var(--brown)}
.util{position:absolute;right:124px;top:12px;display:flex;gap:18px;font-size:11px;color:var(--muted)}
.util span::before{content:"";display:inline-block;width:10px;height:10px;border-radius:50%;background:var(--brown);margin-right:5px;vertical-align:-1px}
.search{position:absolute;right:124px;top:44px;display:flex;gap:6px}
.search .field{width:150px;height:24px;border:1px solid var(--line);background:#fff;border-radius:3px;font-size:10px;color:#aaa;padding:4px 8px}
.search .go{width:44px;height:24px;background:var(--brown);color:#fff;border-radius:3px;font-size:10px;text-align:center;line-height:24px}

.global-nav{height:44px;background:linear-gradient(#fbf8f2,#ece3d3);border-top:1px solid var(--line);border-bottom:1px solid var(--line)}
.global-nav ul{list-style:none;display:flex;justify-content:space-between;width:952px;margin:0 auto;height:100%;align-items:center}
.global-nav li{font-size:13px;font-weight:700;color:var(--brown);flex:1;text-align:center;border-right:1px solid var(--line)}
.global-nav li:last-child{border-right:none}

.hero{position:relative;height:440px;background:linear-gradient(90deg,#a7c47a 0%,#dfe8cf 30%,#f3ede2 50%,#efe7dc 70%,#b9cf98 100%)}
.hero-photo-l{position:absolute;left:0;top:0;width:360px;height:440px;background:radial-gradient(circle at 60% 50%,#c9a160 0%,#7fa84a 45%,#5e8a33 100%)}
.hero-photo-r{position:absolute;right:0;top:0;width:380px;height:440px;background:linear-gradient(160deg,#f1ece4 0%,#d9cfc1 50%,#9fbf70 100%)}
.hero-panel{position:absolute;left:160px;top:40px;width:880px;height:360px;background:rgba(255,255,255,.94);border-radius:180px;display:flex;align-items:center}
.hero-bottle{margin-left:80px;width:100px;height:290px;flex:none;border-radius:18px 18px 10px 10px;background:linear-gradient(90deg,#a8361e,#e36d2c 50%,#a8361e)}
.badge{position:absolute;left:60px;top:36px;width:76px;height:76px;border-radius:50%;background:var(--orange);color:#fff;font-weight:700;text-align:center;font-size:12px;line-height:1.2;padding-top:18px}
.badge b{font-size:20px;display:block}
.hero-copy{margin-left:40px;width:260px;flex:none}
.hero-copy h1{font-family:"Noto Serif JP",serif;font-weight:500;font-size:28px;line-height:1.5;color:var(--brown-dark);white-space:nowrap}
.hero-copy p{font-family:"Noto Serif JP",serif;font-size:17px;color:var(--green-dark);margin-top:10px;white-space:nowrap}
.brand-mark{display:flex;align-items:center;gap:10px;margin-top:12px;font-family:"Noto Serif JP",serif;font-weight:700;font-size:34px;color:var(--brown-dark)}
.brand-mark i{width:22px;height:22px;background:var(--green);border-radius:50%}
.hero-people{position:absolute;right:60px;top:30px;width:270px;height:300px;border-radius:135px;background:linear-gradient(160deg,#fbf6ef,#e8d6c6 60%,#cdb69e)}
.hero-bubble{position:absolute;right:-10px;top:200px;width:116px;height:116px;border-radius:50%;background:#f2c9c9;color:#fff;font-size:12px;text-align:center;padding-top:34px;line-height:1.6;font-weight:700}
.arrow{position:absolute;top:198px;width:40px;height:40px;border-radius:50%;background:var(--green)}
.arrow.prev{left:124px}.arrow.next{right:124px}
.arrow svg{width:40px;height:40px}
.dots{display:flex;justify-content:center;gap:12px;height:44px;align-items:center}
.dots i{width:12px;height:12px;border-radius:50%;background:var(--beige)}
.dots i:first-child{background:var(--brown)}

.wrap{width:952px;margin:12px auto 0;display:flex;gap:20px;height:1640px}
.side{width:224px;flex:none}
.main{flex:1}

.login-btn{height:56px;background:linear-gradient(#8a6a4c,var(--brown-dark));color:#fff;border-radius:6px;font-weight:700;font-size:15px;display:flex;align-items:center;padding-left:20px;gap:10px;margin-top:0}
.login-btn::before{content:"";width:14px;height:14px;border-radius:50%;background:#fff}
.box{background:var(--paper);border:1px solid var(--line);margin-top:22px}
.box h2{background:var(--brown);color:#fff;font-size:13px;padding:8px 12px}
.cat li{list-style:none;border-bottom:1px dotted var(--line);padding:10px 14px 10px 26px;font-size:12px;position:relative}
.cat li::before{content:"";position:absolute;left:12px;top:16px;border:4px solid transparent;border-left-color:var(--green)}
.season li{list-style:none;display:flex;gap:10px;padding:8px 10px;border-bottom:1px dotted var(--line);font-size:11px;align-items:center}
.season .thumb{width:30px;height:40px;flex:none;border-radius:4px;background:linear-gradient(#e7763a,#a8361e)}
.pay p{font-size:11px;padding:10px 12px;color:var(--muted)}
.cards{display:flex;gap:6px;padding:0 12px 12px}
.cards i{width:40px;height:26px;border-radius:3px;background:var(--beige)}
.present{margin-top:22px;height:260px;background:linear-gradient(150deg,#7a2a1c,#b2502d 60%,#d7904a);position:relative}
.present span{position:absolute;left:16px;top:150px;font-family:"Noto Serif JP",serif;font-size:30px;color:#fff;letter-spacing:3px}
.present small{position:absolute;left:16px;top:196px;color:#fff;font-size:11px;line-height:1.5}

.notice{height:30px;border:1px solid var(--line);background:#fff;font-size:11px;display:flex;align-items:center;padding-left:12px;gap:8px}
.notice b{background:var(--red);color:#fff;font-size:10px;padding:1px 6px;border-radius:2px}
.banner-main{margin-top:14px;height:214px;display:flex;border:1px solid var(--line);background:#fff}
.banner-main .copy{width:45%;padding:30px 0 0 30px}
.banner-main .copy h3{font-family:"Noto Serif JP",serif;font-weight:500;font-size:20px;line-height:1.6;color:var(--brown-dark)}
.banner-main .copy .brand-mark{font-size:26px}
.banner-main .ph{flex:1;background:linear-gradient(140deg,#fbf7f0,#ead9c8 60%,#c7d9a9)}
.banner-row{display:flex;gap:12px;margin-top:12px;height:150px}
.banner-row .bn{flex:1;position:relative;padding:22px;font-family:"Noto Serif JP",serif;font-size:16px;line-height:1.6;color:#fff}
.bn.dark{background:linear-gradient(90deg,#2b2218,#6b4a2a)}
.bn.olive{background:linear-gradient(90deg,#5f7a2e,#a9c16c)}
.bn.pinkish{background:linear-gradient(90deg,#f6e7e3,#e8c6c0);color:var(--brown-dark)}
.bn.green2{background:linear-gradient(90deg,#3f6a2a,#7ea24a)}

.product-sec{margin-top:20px;background:#fff;border:1px solid var(--line);height:310px;padding:14px 18px}
.sec-head{display:flex;justify-content:space-between;align-items:center;border-bottom:2px solid var(--beige);padding-bottom:8px}
.sec-head h2{font-family:"Noto Serif JP",serif;font-size:20px;color:var(--brown-dark);display:flex;align-items:center;gap:8px}
.sec-head h2 i{width:20px;height:20px;border-radius:50%;background:var(--orange)}
.sec-head .more{background:var(--green);color:#fff;font-size:10px;padding:4px 12px;border-radius:12px}
.products{display:flex;justify-content:space-between;margin-top:18px}
.item{width:100px;text-align:left;font-size:10px;line-height:1.4}
.item .pic{height:140px;display:flex;align-items:flex-end;justify-content:center;position:relative}
.item .rank{position:absolute;left:0;top:0;width:24px;height:24px;border-radius:50%;background:var(--green);color:#fff;font-size:12px;text-align:center;line-height:24px;font-weight:700}
.item .b{width:36px;border-radius:6px 6px 3px 3px}
.b.bottle{height:120px;background:linear-gradient(90deg,#a8361e,#e36d2c,#a8361e)}
.b.tube{height:110px;background:linear-gradient(#eee2c8,#c99a5a);width:30px;border-radius:3px 3px 10px 10px}
.b.pack{height:90px;width:80px;background:linear-gradient(#f1e6f0,#d9c1cf);border-radius:4px}
.item p{margin-top:8px}
.item .price{color:var(--red);font-weight:700}

.site-footer{height:166px;background:#fff;border-top:4px solid var(--brown);margin-top:16px}
.foot-nav{display:flex;justify-content:center;gap:30px;font-size:11px;padding:14px 0;border-bottom:1px solid var(--line)}
.site-footer .logo{position:static;font-size:28px;margin-top:26px}
.copy-r{text-align:center;font-size:10px;color:var(--muted);margin-top:6px}
</style>
</head>
<body>
<header class="site-header">
  <p class="tagline">自然のチカラで、<br>毎日の肌にやさしさを。</p>
  <div class="logo">KAZANEMORI</div>
  <div class="util"><span>サイトマップ</span><span>カートを見る</span></div>
  <div class="search"><div class="field">商品検索</div><div class="go">検索</div></div>
</header>
<nav class="global-nav"><ul>
  <li>クレンジング</li><li>洗顔</li><li>化粧水</li><li>美容液</li><li>クリーム</li><li>メイク</li><li>ヘアケア</li><li>ボディケア</li><li>その他</li>
</ul></nav>

<section class="hero">
  <div class="hero-photo-l" role="img" aria-label="柑橘と緑の葉の写真"></div>
  <div class="hero-photo-r" role="img" aria-label="自然光の中の母子の写真"></div>
  <div class="hero-panel">
    <div class="badge">天然<b>100%</b></div>
    <div class="hero-bottle" role="img" aria-label="オイル美容液ボトルの写真"></div>
    <div class="hero-copy">
      <h1>自然のチカラで<br>美しい肌に導く</h1>
      <p>オーガニックスキンケア</p>
      <div class="brand-mark"><i></i>森花詩</div>
    </div>
    <div class="hero-people" role="img" aria-label="赤ちゃんを抱く母親の写真"></div>
    <div class="hero-bubble">家族で使える<br>やさしさ</div>
  </div>
  <a class="arrow prev"><svg viewBox="0 0 40 40"><path d="M23 12l-8 8 8 8" stroke="#fff" stroke-width="3" fill="none"/></svg></a>
  <a class="arrow next"><svg viewBox="0 0 40 40"><path d="M17 12l8 8-8 8" stroke="#fff" stroke-width="3" fill="none"/></svg></a>
</section>
<div class="dots"><i></i><i></i><i></i><i></i></div>

<div class="wrap">
  <aside class="side">
    <a class="login-btn">会員ページログイン</a>
    <div class="box">
      <h2>商品を探す</h2>
      <ul class="cat">
        <li>全ての商品</li><li>クレンジング</li><li>洗顔</li><li>化粧水</li><li>美容液</li><li>クリーム</li><li>メイク</li><li>ヘアケア</li><li>ボディケア</li><li>その他</li>
      </ul>
    </div>
    <div class="box">
      <h2>季節のお勧め</h2>
      <ul class="season">
        <li><span class="thumb" role="img" aria-label="商品写真"></span>ナチュラル フェイスオイル 30ml</li>
        <li><span class="thumb" role="img" aria-label="商品写真"></span>ナチュラル ボディオイル 100ml</li>
        <li><span class="thumb" role="img" aria-label="商品写真"></span>保湿 ハンドクリーム 50g</li>
        <li><span class="thumb" role="img" aria-label="商品写真"></span>ナチュラル クレンジング 150ml</li>
        <li><span class="thumb" role="img" aria-label="商品写真"></span>やさしい 化粧水 120ml</li>
        <li><span class="thumb" role="img" aria-label="商品写真"></span>ナチュラル ヘアオイル 60ml</li>
      </ul>
    </div>
    <div class="box pay">
      <h2>お支払い</h2>
      <p>各種カード・代金引換・銀行振込がご利用いただけます。</p>
      <div class="cards"><i></i><i></i><i></i><i></i></div>
    </div>
    <div class="present" role="img" aria-label="プレゼント企画の商品写真">
      <span>PRESENT</span>
      <small>ご購入の方に毎月抽選で<br>ミニボトルをプレゼント</small>
    </div>
  </aside>

  <main class="main">
    <div class="notice"><b>NEWS</b>ただいま新商品を開発中です。発売日は決まり次第お知らせします。</div>
    <div class="banner-main">
      <div class="copy">
        <h3>自然のチカラで<br>美しい肌に導く</h3>
        <div class="brand-mark"><i></i>森花詩</div>
      </div>
      <div class="ph" role="img" aria-label="母親と赤ちゃんの写真"></div>
    </div>
    <div class="banner-row">
      <div class="bn dark" role="img" aria-label="ボトルと黒背景の商品写真">極上のうるおい<br>美容オイル</div>
      <div class="bn olive" role="img" aria-label="木漏れ日と緑の写真">自然に寄り添う<br>スキンケア</div>
    </div>
    <div class="banner-row">
      <div class="bn green2" role="img" aria-label="森とボトルの写真">自然生まれの素材で<br>毎日のお手入れを</div>
      <div class="bn pinkish" role="img" aria-label="母子の写真">家族みんなに<br>やさしい肌ケア</div>
    </div>

    <section class="product-sec">
      <div class="sec-head"><h2><i></i>人気ランキング</h2><span class="more">人気ランキングをもっと見る</span></div>
      <div class="products">
        <div class="item"><div class="pic"><span class="rank">1</span><span class="b bottle" role="img" aria-label="商品写真"></span></div><p>森花詩 フェイスオイル 30ml</p><p class="price">3,150円(税込)</p></div>
        <div class="item"><div class="pic"><span class="rank">2</span><span class="b tube" role="img" aria-label="商品写真"></span></div><p>森花詩 ナチュラル 洗顔フォーム</p><p class="price">1,890円(税込)</p></div>
        <div class="item"><div class="pic"><span class="rank">3</span><span class="b pack" role="img" aria-label="商品写真"></span></div><p>森花詩 お試し セット</p><p class="price">2,100円(税込)</p></div>
        <div class="item"><div class="pic"><span class="rank">4</span><span class="b pack" role="img" aria-label="商品写真"></span></div><p>森花詩 保湿 マスク 5枚</p><p class="price">1,575円(税込)</p></div>
        <div class="item"><div class="pic"><span class="rank">5</span><span class="b tube" role="img" aria-label="商品写真"></span></div><p>森花詩 ハンド クリーム</p><p class="price">1,260円(税込)</p></div>
        <div class="item"><div class="pic"><span class="rank">6</span><span class="b bottle" role="img" aria-label="商品写真"></span></div><p>森花詩 ボディオイル 100ml</p><p class="price">4,200円(税込)</p></div>
      </div>
    </section>

    <section class="product-sec">
      <div class="sec-head"><h2><i></i>おすすめ商品</h2><span class="more">おすすめ商品をもっと見る</span></div>
      <div class="products">
        <div class="item"><div class="pic"><span class="b bottle" role="img" aria-label="商品写真"></span></div><p>森花詩 フェイスオイル 30ml</p><p class="price">3,150円(税込)</p></div>
        <div class="item"><div class="pic"><span class="b tube" role="img" aria-label="商品写真"></span></div><p>森花詩 ナチュラル 洗顔フォーム</p><p class="price">1,890円(税込)</p></div>
        <div class="item"><div class="pic"><span class="b bottle" role="img" aria-label="商品写真"></span></div><p>森花詩 ヘアオイル 60ml</p><p class="price">2,520円(税込)</p></div>
        <div class="item"><div class="pic"><span class="b pack" role="img" aria-label="商品写真"></span></div><p>森花詩 保湿 マスク 5枚</p><p class="price">1,575円(税込)</p></div>
        <div class="item"><div class="pic"><span class="b tube" role="img" aria-label="商品写真"></span></div><p>森花詩 ハンド クリーム</p><p class="price">1,260円(税込)</p></div>
        <div class="item"><div class="pic"><span class="b bottle" role="img" aria-label="商品写真"></span></div><p>森花詩 ボディオイル 100ml</p><p class="price">4,200円(税込)</p></div>
      </div>
    </section>

    <section class="product-sec">
      <div class="sec-head"><h2><i></i>最近チェックした商品</h2><span class="more">チェックした商品を見る</span></div>
      <div class="products">
        <div class="item"><div class="pic"><span class="b bottle" role="img" aria-label="商品写真"></span></div><p>森花詩 フェイスオイル 30ml</p><p class="price">3,150円(税込)</p></div>
        <div class="item"><div class="pic"><span class="b tube" role="img" aria-label="商品写真"></span></div><p>森花詩 ナチュラル 洗顔フォーム</p><p class="price">1,890円(税込)</p></div>
        <div class="item"><div class="pic"><span class="b pack" role="img" aria-label="商品写真"></span></div><p>森花詩 お試し セット</p><p class="price">2,100円(税込)</p></div>
        <div class="item"><div class="pic"><span class="b pack" role="img" aria-label="商品写真"></span></div><p>森花詩 保湿 マスク 5枚</p><p class="price">1,575円(税込)</p></div>
        <div class="item"><div class="pic"><span class="b tube" role="img" aria-label="商品写真"></span></div><p>森花詩 ハンド クリーム</p><p class="price">1,260円(税込)</p></div>
        <div class="item"><div class="pic"><span class="b bottle" role="img" aria-label="商品写真"></span></div><p>森花詩 ボディオイル 100ml</p><p class="price">4,200円(税込)</p></div>
      </div>
    </section>
  </main>
</div>

<footer class="site-footer">
  <div class="foot-nav"><span>ホーム</span><span>サイトマップ</span><span>お問い合わせ</span><span>プライバシーポリシー</span><span>ご利用ガイド</span><span>特定商取引法に基づく表記</span><span>会社概要</span></div>
  <div class="logo">KAZANEMORI</div>
  <p class="copy-r">Copyright © KAZANEMORI Co.,Ltd. All Rights Reserved.</p>
</footer>
</body>
</html>
```